Fernbrook Plots - Online-only garden installation company

Online-only garden installation company. Our demographic is middle aged / suburban women, and we anticipate Facebook driving traffic to this website, as well as referrals from garden centers. The website must be very simple in design and function.

All orders will be placed through the website, including size of garden (3 options), location in yard, payment, and scheduling of installation date.

The website should employ a 3 step process:

Step 1: Select garden size. Either an 4' X 4', 8' X 4', or 12' X 4'.

Step 2: Select a location. We would like to use google maps to look up a US address, then "drag and drop" one of the garden sizes from step 1 to the location the customer would like us to install the garden at their home.

Step 3: Pick an installation date and pay. Using an online calendar the customer will pick a date, and then pay for the installation via credit card.

The website will be linked to an email account, FernbrookPlots@mailzy.com to inform us of orders placed.

Target Market(s)

Our demographic is middle aged / suburban women, and we anticipate Facebook driving traffic to this website, as well as referrals from garden centers.

Industry/Entity Type

Coding

Number of Pages Required

Requirements
Must have
• Scheduling and payment options.

```html
<!DOCTYPE html>
<html lang="en">
<head>
<meta charset="utf-8">
<title>Fernbrook Plots – Garden Installation</title>
<link href="https://fonts.googleapis.com/css2?family=Bitter:wght@400;700&family=Signika:wght@400&family=Open+Sans:wght@400;600&display=swap" rel="stylesheet">
<style>
:root{
  --green:#3b8a3c;
  --green-dark:#2f7a31;
  --orange:#e8562a;
  --orange-dark:#c9401a;
  --ink:#222;
  --muted:#555;
  --line:#d8d8d8;
}
*{box-sizing:border-box;margin:0;padding:0}
html,body{width:1021px;height:1200px;overflow:hidden;background:#fff}
body{position:relative;font-family:"Open Sans",Arial,sans-serif;color:var(--ink)}

.site-header{position:absolute;left:0;top:0;width:1021px;height:114px;background:#fff;z-index:2}
.brand{position:absolute;left:74px;top:0;width:158px;height:148px;background:#fff;
  clip-path:polygon(0 0,100% 0,100% 70%,50% 100%,0 70%);display:flex;align-items:center;justify-content:center;gap:6px}
.brand-mark{width:10px;height:10px;background:var(--orange)}
.brand-name{font-family:"Bitter",serif;font-size:17px;font-weight:700;color:var(--ink);letter-spacing:.5px}
.help{position:absolute;right:78px;top:24px;display:flex;align-items:center;gap:10px}
.help-text{font-family:Arial,sans-serif;font-size:10.5px;color:var(--orange)}
.help-phone{font-family:Arial,sans-serif;font-size:20px;color:var(--ink)}
.main-nav{position:absolute;right:76px;top:76px;display:flex;font-family:"Bitter",serif;font-size:13px}
.main-nav a{color:var(--ink);text-decoration:none;padding:0 25px;border-left:1px solid var(--line);line-height:14px;white-space:nowrap}
.main-nav a:first-child{border-left:none}
.main-nav a:last-child{padding-right:0}
.main-nav a.active{color:var(--orange)}

.hero{position:absolute;left:0;top:114px;width:1021px;height:397px;
  background:linear-gradient(125deg,#e4e4e4 0%,#f6f6f6 35%,#ebebeb 60%,#f7f7f7 100%)}
.hero-title{position:absolute;left:70px;top:145px;font-family:"Signika",sans-serif;font-size:37px;line-height:51px;color:var(--green);font-weight:400}
.hero-image{position:absolute;left:518px;top:58px;width:412px;height:282px;border-radius:6px;
  background:linear-gradient(160deg,#6a9a3c 0%,#c9a24a 45%,#d8cbb4 70%,#bdb3a4 100%)}
.hero-arrow{position:absolute;top:206px}
.hero-arrow.prev{left:26px}
.hero-arrow.next{right:26px}

.sizes{position:absolute;left:0;top:540px;width:1021px;text-align:center}
.section-title{font-family:"Bitter",serif;font-size:25px;font-weight:700;color:var(--ink)}
.section-rule{width:78px;height:2px;background:var(--green);margin:10px auto 0}
.card{position:absolute;top:73px;width:280px;height:257px;border:1px solid var(--line);background:#fff}
.card-image{position:absolute;left:40px;top:22px;width:200px;height:160px;border-radius:4px;
  background:linear-gradient(180deg,#3f7f34 0%,#5f9c41 50%,#cfb07a 80%,#b8955c 100%)}
.card-caption{position:absolute;left:0;right:0;top:197px;font-family:Arial,sans-serif;font-size:13.5px;color:var(--ink)}
.card-bar{position:absolute;left:-1px;right:-1px;bottom:-1px;height:30px;background:var(--orange);display:flex;align-items:center;padding:0 8px 0 10px;color:#fff}
.card-size{font-family:Arial,sans-serif;font-size:13.5px;flex:1;text-align:left;white-space:nowrap}
.card-price{background:var(--orange-dark);border-radius:3px;font-family:"Open Sans",sans-serif;font-weight:600;font-size:12.5px;line-height:22px;height:22px;width:67px;text-align:center;margin-right:7px;white-space:nowrap}
.card-buy{background:var(--orange-dark);border-radius:3px;font-size:10.5px;line-height:22px;height:22px;width:90px;display:flex;align-items:center;justify-content:center;gap:6px;white-space:nowrap}

.site-footer{position:absolute;left:0;top:934px;width:1021px;height:228px;border-radius:30px 30px 0 0;
  background:linear-gradient(100deg,#1f2a19 0%,#2b3a22 45%,#3b3a26 70%,#5a4330 100%);color:#fff}
.footer-col{position:absolute;top:30px}
.footer-head{font-family:"Bitter",serif;font-size:14.5px;font-weight:400;padding-bottom:9px;border-bottom:1px solid rgba(255,255,255,.2);margin-bottom:12px}
.about{left:70px;width:214px}
.about p{font-family:Arial,sans-serif;font-size:10.8px;line-height:18.3px}
.contact{left:330px;width:184px}
.contact-line{display:flex;align-items:center;gap:8px;font-size:11.5px;margin-bottom:12px}
.social{display:flex;gap:6px}
.social span{width:25px;height:25px;display:block}
.newsletter{left:556px;width:182px}
.newsletter p{font-size:10.5px;line-height:15px;margin-bottom:10px}
.email-field{width:168px;height:22px;background:#fff;border-radius:3px;color:#333;font-size:10px;padding:4px 6px}
.subscribe{display:inline-block;margin-top:13px;background:var(--green);font-family:Arial,sans-serif;font-size:12px;padding:5px 14px;border-radius:2px}
.footer-brand{position:absolute;left:770px;top:106px;font-family:"Bitter",serif;font-size:18px;font-weight:700;color:rgba(255,255,255,.45)}

.copyright-bar{position:absolute;left:0;top:1162px;width:1021px;height:38px;background:var(--green);color:#fff;display:flex;align-items:center;padding:0 70px;font-family:"Bitter",serif;font-size:11px}
.copyright-bar .spacer{flex:1}
.pay{display:flex;gap:6px;margin-left:14px}
.pay span{width:30px;height:18px;background:#fff;border-radius:2px;display:block}
</style>
</head>
<body>
<header class="site-header">
  <div class="brand"><span class="brand-mark"></span><span class="brand-name">Fernbrook Plots</span></div>
  <div class="help">
    <span class="help-text">Need any help? Call Us Anytime</span>
    <svg width="26" height="26" viewBox="0 0 24 24"><path fill="#3b8a3c" d="M6.6 10.8a15 15 0 0 0 6.6 6.6l2.2-2.2c.3-.3.7-.4 1-.2 1.1.4 2.3.6 3.6.6.6 0 1 .4 1 1V20c0 .6-.4 1-1 1A17 17 0 0 1 3 4c0-.6.4-1 1-1h3.5c.6 0 1 .4 1 1 0 1.3.2 2.5.6 3.6.1.3 0 .7-.2 1z"/></svg>
    <span class="help-phone">123-456-7890</span>
  </div>
  <nav class="main-nav">
    <a class="active" href="#">HOME</a><a href="#">How We Work</a><a href="#">BASKET</a><a href="#">CONTACT US</a>
  </nav>
</header>

<section class="hero">
  <h1 class="hero-title">We Are Online-only<br>Garden Installation<br>Company</h1>
  <div class="hero-image" role="img" aria-label="Raised metal garden bed planted with colourful flowers"></div>
  <svg class="hero-arrow prev" width="22" height="40" viewBox="0 0 22 40"><path d="M20 1 2 20l18 19" fill="none" stroke="#888" stroke-width="1.5"/></svg>
  <svg class="hero-arrow next" width="22" height="40" viewBox="0 0 22 40"><path d="M2 1l18 19L2 39" fill="none" stroke="#888" stroke-width="1.5"/></svg>
</section>

<section class="sizes">
  <h2 class="section-title">Select Size Of The Garden</h2>
  <div class="section-rule"></div>

  <div class="card" style="left:68px">
    <div class="card-image" role="img" aria-label="Wooden raised bed with vegetable plants"></div>
    <div class="card-caption">Lorem Ispum is the Dummy Text</div>
    <div class="card-bar"><span class="card-size">Size : 4' X 4'</span><span class="card-price">$175.00</span><span class="card-buy"><svg width="12" height="10" viewBox="0 0 12 10"><path d="M0 1h2l2 6h6l1.5-4.5H3" fill="none" stroke="#fff" stroke-width="1.4"/><circle cx="4.5" cy="9" r="1" fill="#fff"/><circle cx="9.5" cy="9" r="1" fill="#fff"/></svg>Buy Now</span></div>
  </div>

  <div class="card" style="left:370px">
    <div class="card-image" role="img" aria-label="Wooden raised bed with vegetable plants"></div>
    <div class="card-bar"><span class="card-size">Size : 8' X 4'</span><span class="card-price">$275.00</span><span class="card-buy"><svg width="12" height="10" viewBox="0 0 12 10"><path d="M0 1h2l2 6h6l1.5-4.5H3" fill="none" stroke="#fff" stroke-width="1.4"/><circle cx="4.5" cy="9" r="1" fill="#fff"/><circle cx="9.5" cy="9" r="1" fill="#fff"/></svg>Buy Now</span></div>
  </div>

  <div class="card" style="left:673px">
    <div class="card-image" role="img" aria-label="Wooden raised bed with vegetable plants"></div>
    <div class="card-bar"><span class="card-size">Size : 12' X 4'</span><span class="card-price">$375.00</span><span class="card-buy"><svg width="12" height="10" viewBox="0 0 12 10"><path d="M0 1h2l2 6h6l1.5-4.5H3" fill="none" stroke="#fff" stroke-width="1.4"/><circle cx="4.5" cy="9" r="1" fill="#fff"/><circle cx="9.5" cy="9" r="1" fill="#fff"/></svg>Buy Now</span></div>
  </div>
</section>

<footer class="site-footer" role="img" aria-label="Background of freshly harvested carrots in soil">
  <div class="footer-col about">
    <h3 class="footer-head">About Us</h3>
    <p>Lorem ipsum dolor rrsit amet, consectetuer adipiscing efdflit, sed diarm nonummy nibh euismod tincidunt ut laoreet dolona aliquam erat volutpat. Ut wisi enim ad mim ventirrm, quis nostrud exerci tation ullamcer surscipit lo Duis autem vel eum iriure drelor iendrerit in vulputate velit esse molestie conquat, vel illum dolore eu feugiat nulla.</p>
  </div>
  <div class="footer-col contact">
    <h3 class="footer-head">Contact Info</h3>
    <div class="contact-line"><svg width="11" height="11" viewBox="0 0 24 24"><path fill="#3b8a3c" d="M6.6 10.8a15 15 0 0 0 6.6 6.6l2.2-2.2c.3-.3.7-.4 1-.2 1.1.4 2.3.6 3.6.6.6 0 1 .4 1 1V20c0 .6-.4 1-1 1A17 17 0 0 1 3 4c0-.6.4-1 1-1h3.5c.6 0 1 .4 1 1 0 1.3.2 2.5.6 3.6.1.3 0 .7-.2 1z"/></svg>123 - 456 - 7890</div>
    <div class="contact-line"><svg width="12" height="9" viewBox="0 0 12 9"><rect x=".5" y=".5" width="11" height="8" fill="none" stroke="#3b8a3c"/><path d="M.5.5 6 5l5.5-4.5" fill="none" stroke="#3b8a3c"/></svg>info@fernbrookplots.com</div>
    <h3 class="footer-head" style="margin-top:22px">Social Media</h3>
    <div class="social"><span style="background:#3b5998"></span><span style="background:#0e76a8"></span><span style="background:#d34836"></span><span style="background:#cc2020"></span></div>
  </div>
  <div class="footer-col newsletter">
    <h3 class="footer-head" style="border:none">Newsletter Signup</h3>
    <p>Get latest updates by entering your email address</p>
    <div class="email-field">Email Address</div>
    <span class="subscribe">SUBSCRIBE</span>
  </div>
  <div class="footer-brand">Fernbrook Plots</div>
</footer>

<div class="copyright-bar">
  <span>Copyright © 2017 FERNBROOK PLOTS. All Rights Reserved.</span>
  <span class="spacer"></span>
  <span>We Accept</span>
  <span class="pay"><span></span><span></span><span></span></span>
</div>
</body>
</html>
```